Industrial services company requires brochure for new product

We are an industrial services company called Tern Valley Holdings. Our clients include major mining, oil and gas and infrastructure clients in Western Australia.

We require a 4 page brochure to feature a new paint removal machine we are bringing to the market in Western Australia.The document will be used predominantly electronically but should be of a quality that can be printed also.

The new machine is an innovative way of removing paint from steel structures as it does not use abrasive blasting to remove the paint. Instead it uses induction heating.

There are some major environmental and safety benefits to using this machine over traditional methods as there are no airborne particles, no noise and minimal waste. The environmental and safety benefits of the are the competitive advantage of the machine and should come through in the marketing.

I have provided as an attachment the proposed copy, the pics available for use, and the Tern Valley logo.

In general I am thinking page 1 (cover - hero pic/company logo), page 2 (machine information), page 3 (case study) page 4 (about us/contact details/logo etc) but am happy to look at other options.

The images I have attached are the highest quality I will have available.

Target Market(s)

Mining, oil and gas, government infrastructure clients. These are businesses

Industry/Entity Type

Oil And Gas

Requirements
Must have
• The majority of the text supplied as necessary to understand the technology.

```html
<!DOCTYPE html>
<html lang="en">
<head>
<meta charset="utf-8">
<title>Tern Valley – The Thermal Coat Lifter – Cover Options</title>
<link rel="stylesheet" href="https://fonts.googleapis.com/css2?family=PT+Sans:wght@400;700&family=Arimo:wght@400&display=swap">
<style>
  :root {
    --board-light: #6e6a71;
    --board-dark: #48454a;
    --paper: #ffffff;
    --brand-blue: #1c9ad8;
    --brand-blue-text: #1d8fcf;
    --ink-white: #ffffff;
    --label: #f2f2f2;
    --photo-sky: #c9c6bd;
    --photo-steel: #8b6a48;
    --photo-deck: #4a3f35;
    --photo-water: #2f3935;
    --accent-rule: #c7583a;
  }
  * { box-sizing: border-box; margin: 0; padding: 0; }
  html, body { width: 1200px; height: 960px; overflow: hidden; }
  body {
    position: relative;
    background: radial-gradient(ellipse at 50% 35%, var(--board-light) 0%, var(--board-dark) 100%);
    font-family: "PT Sans", sans-serif;
  }
  .cover {
    position: absolute;
    top: 161px;
    height: 574px;
    background: var(--paper);
    box-shadow: 6px 10px 22px rgba(0,0,0,0.45);
    overflow: hidden;
  }
  .cover--a { left: 148px; width: 445px; }
  .cover--b { left: 650px; width: 443px; }

  .brand {
    position: absolute;
    top: 26px;
    left: 20px;
    display: flex;
    align-items: center;
    gap: 8px;
  }
  .brand__dot {
    width: 32px; height: 32px;
    border-radius: 50%;
    background: var(--brand-blue);
  }
  .brand__name {
    font-family: "PT Sans", sans-serif;
    font-weight: 700;
    font-size: 21px;
    color: var(--brand-blue-text);
    letter-spacing: 0.3px;
  }

  .hero-photo {
    position: absolute;
    left: 0;
    top: 69px;
    width: 100%;
    background: linear-gradient(180deg,
      var(--photo-sky) 0%,
      var(--photo-steel) 28%,
      var(--photo-deck) 45%,
      #2b2723 62%,
      var(--photo-water) 100%);
  }
  .cover--a .hero-photo { height: 422px; }
  .cover--b .hero-photo { height: 435px; border-bottom: 2px solid var(--accent-rule); }

  .title-band {
    position: absolute;
    left: 0;
    width: 100%;
    background: var(--brand-blue);
    color: var(--ink-white);
    padding-left: 18px;
  }
  .cover--a .title-band { top: 491px; height: 83px; padding-top: 12px; }
  .cover--b .title-band { top: 389px; height: 71px; padding-top: 6px; }

  .title-band__heading {
    font-family: "PT Sans", sans-serif;
    font-weight: 700;
    font-size: 16.5px;
    letter-spacing: 1.6px;
  }
  .title-band__quote {
    margin-top: 8px;
    font-family: "Arimo", sans-serif;
    font-size: 11.5px;
    line-height: 15px;
  }
  .cover--b .title-band__quote { margin-top: 5px; }

  .option-label {
    position: absolute;
    top: 776px;
    width: 240px;
    text-align: center;
    font-family: "PT Sans", sans-serif;
    font-size: 27px;
    letter-spacing: 1px;
    color: var(--label);
  }
  .option-label--a { left: 250px; }
  .option-label--b { left: 766px; }
</style>
</head>
<body>

  <section class="cover cover--a">
    <div class="brand">
      <span class="brand__dot"></span>
      <span class="brand__name">Tern Valley</span>
    </div>
    <div class="hero-photo" role="img" aria-label="Photo of a coastal wharf structure with scaffolding, steel beams and a large white pipe above the water"></div>
    <div class="title-band">
      <h1 class="title-band__heading">The Thermal Coat Lifter</h1>
      <p class="title-band__quote">“ A cleaner, quieter and far safer approach to stripping<br>&nbsp;hazardous paint and coatings from structural steelwork ”</p>
    </div>
  </section>

  <section class="cover cover--b">
    <div class="brand">
      <span class="brand__dot"></span>
      <span class="brand__name">Tern Valley</span>
    </div>
    <div class="hero-photo" role="img" aria-label="Photo of a coastal wharf structure with scaffolding, steel beams and a large white pipe above the water"></div>
    <div class="title-band">
      <h1 class="title-band__heading">The Thermal Coat Lifter</h1>
      <p class="title-band__quote">“ A cleaner, quieter and far safer approach to stripping<br>&nbsp;hazardous paint and coatings from structural steelwork ”</p>
    </div>
  </section>

  <p class="option-label option-label--a">DESIGN A</p>
  <p class="option-label option-label--b">DESIGN B</p>

</body>
</html>
```